Easter Competition Flyer to Healthcare Clients with a chance to win 1 of 2 luxury hampers

An A5 promotional flyer to send to our clients for an Easter competition with the chance to win some Easter Egg /Chocolate hampers. For every shift booked between 19th - 22nd April they will be entered into a draw with the chance to win 1 of 3 prizes available consisting of Easter Egg/Chocolate hampers (images attached)

Target Market(s)

Current and potential clients in the Healthcare Sector

Industry/Entity Type

Healthcare

Font styles to use
Decorative
Script

Colors

Designer to choose colors to be used in the design.

Requirements
Must have
• Company logo, Company colours, Branch contact details - To book call us now on Maidstone 01555 318407, Tonbridge 01555 826153, Ashford 01555 694372, Dartford 01555 203918 Website - www.carewillowstaffing.co.uk, Details of the competition (For every shift booked between 19th - 22nd April you will automatically be entered into our Easter prize draw for a chance to win 1 of 3 luxury Easter Hampers) - 3 available, pictures similar to prizes (images attached)
Nice to have
• Its a fun competitions so open to some fun Easter pictures of eggs and bunnies and other Easter related images
Should not have
• Too serious or corporate feel to it

```html
<!DOCTYPE html>
<html lang="en">
<head>
<meta charset="utf-8">
<title>Easter Party Flyer</title>
<link rel="stylesheet" href="https://fonts.googleapis.com/css2?family=Kaushan+Script&family=Pathway+Gothic+One&family=Montserrat:wght@500&display=swap">
<style>
  :root{
    --navy:#1f4aa0;
    --teal:#1fa88a;
    --ink:#1d1d2b;
    --sky-top:#23b0ec;
    --sky-mid:#bfe7fb;
    --paper:#ffffff;
    --stage:#ecebe8;
    --grass:#5cbf2a;
    --egg:#2ea889;
  }
  *{margin:0;padding:0;box-sizing:border-box}
  html,body{width:1170px;height:1200px;overflow:hidden;background:var(--stage)}
  .flyer{
    position:absolute;left:245px;top:123px;width:680px;height:953px;overflow:hidden;
    background:linear-gradient(180deg,var(--sky-top) 0%,#6ccdf4 20%,var(--sky-mid) 42%,#eef8fe 62%,var(--paper) 78%);
    box-shadow:0 6px 24px rgba(0,0,0,.18);
    font-family:"Pathway Gothic One",sans-serif;
  }
  .title{position:absolute;font-family:"Kaushan Script",cursive;line-height:1;white-space:nowrap}
  .title-easter{left:70px;top:30px;font-size:170px;color:var(--navy);text-shadow:4px 4px 0 rgba(255,255,255,.7)}
  .title-party{left:160px;top:190px;font-size:175px;color:var(--teal);text-shadow:4px 4px 0 rgba(255,255,255,.7)}
  .centered{position:absolute;left:0;width:680px;text-align:center;white-space:nowrap}
  .intro{top:346px;font-size:17px;color:var(--ink);padding-left:10px}
  .dates{top:362px;font-size:31px;color:var(--teal);letter-spacing:.5px;padding-left:10px}
  .entry{top:405px;font-size:19px;color:var(--ink);padding-left:8px}
  .prize{top:430px;font-size:22px;color:var(--ink);letter-spacing:.3px}
  .prize .hl{color:var(--navy);font-size:24px}
  .prize-art{position:absolute;left:190px;top:470px;width:305px;height:245px}
  .contact{position:absolute;left:290px;top:718px;width:300px;text-align:center;font-size:16px;line-height:21px;color:var(--ink);letter-spacing:.3px}
  .contact .lead{color:var(--teal)}
  .contact .branch{color:var(--navy)}
  .brand{position:absolute;left:98px;top:728px;display:flex;align-items:center;gap:8px}
  .brand-dot{width:18px;height:18px;border-radius:50%;background:var(--teal)}
  .brand-name{font-size:30px;color:var(--navy)}
  .web{top:787px;font-family:"Montserrat",sans-serif;font-weight:500;font-size:12px;letter-spacing:3.2px;color:var(--ink)}
  .meadow{position:absolute;left:0;bottom:0;width:680px;height:175px;
    background:linear-gradient(180deg,rgba(255,255,255,0) 0%,#a9dd7a 40%,var(--grass) 100%)}
</style>
</head>
<body>
  <main class="flyer">
    <div class="title title-easter">Easter</div>
    <div class="title title-party">Party</div>

    <p class="centered intro">For every shift booked between</p>
    <p class="centered dates">19TH – 22ND APRIL</p>
    <p class="centered entry">you will automatically be entered into our</p>
    <p class="centered prize"><span class="hl">EASTER PRIZE DRAW</span> for a chance to win <span class="hl">1 OF 3 LUXURY EASTER HAMPERS</span></p>

    <svg class="prize-art" viewBox="0 0 305 245" role="img" aria-label="Cartoon bunny holding three egg-shaped frames showing chocolate Easter hampers">
      <ellipse cx="152" cy="60" rx="42" ry="50" fill="#2f4fa8"/>
      <ellipse cx="57" cy="112" rx="55" ry="68" fill="var(--egg)"/>
      <ellipse cx="247" cy="112" rx="55" ry="68" fill="var(--egg)"/>
      <ellipse cx="152" cy="170" rx="55" ry="72" fill="var(--egg)"/>
    </svg>

    <div class="brand">
      <span class="brand-dot"></span>
      <span class="brand-name">CareWillow</span>
    </div>

    <div class="contact">
      <div class="lead">Branch Contact Details – To book call us now on</div>
      <div><span class="branch">MAIDSTONE</span> 01555 318407, <span class="branch">TONBRIDGE</span> 01555 826153,</div>
      <div><span class="branch">ASHFORD</span> 01555 694372, <span class="branch">DARTFORD</span> 01555 203918</div>
    </div>

    <p class="centered web">www.carewillowstaffing.co.uk</p>

    <div class="meadow" role="img" aria-label="Grass meadow with daisies and painted Easter eggs"></div>
  </main>
</body>
</html>
```